We need a web site design that is connected to Talbrook Roofing an American company, Veteran owned. Specializing in new roofs of all kinds, repair existing roofs and emergency roof repairs. located in the north Georgia mountains

Target Market(s)

homeowners end users, real estate, home owners insurance companies

Industry/Entity Type

roofing

Contact Information for Business Card

logo, Veteran owned, supports veteran charities, phone number ect

Font styles to use
Serif

Requirements
Should not have
• na

```html
<!DOCTYPE html>
<html lang="en">
<head>
<meta charset="utf-8">
<title>Talbrook Roofing – Business Card</title>
<link rel="stylesheet" href="https://fonts.googleapis.com/css2?family=Lora:wght@400;500;700&display=swap">
<style>
  :root {
    --backdrop: #3b3b3d;
    --card: #ffffff;
    --brand-red: #e2321f;
    --brand-gold: #c98a1c;
    --ink: #3a3a3a;
  }
  * { box-sizing: border-box; margin: 0; padding: 0; }
  html, body { width: 1200px; height: 1059px; overflow: hidden; }
  body {
    background: var(--backdrop);
    font-family: "Lora", Georgia, serif;
    position: relative;
  }
  .card {
    position: absolute;
    left: 255px;
    width: 690px;
    height: 394px;
    background: var(--card);
    border-radius: 22px;
  }
  .card--front { top: 100px; }
  .card--back { top: 537px; }

  .brand {
    position: absolute;
    display: flex;
    flex-direction: column;
    align-items: center;
    text-align: center;
  }
  .brand__name {
    display: flex;
    align-items: center;
    gap: 10px;
    color: var(--brand-red);
    font-weight: 700;
    text-transform: uppercase;
    white-space: nowrap;
  }
  .brand__dot {
    border-radius: 50%;
    background: var(--brand-red);
    flex: none;
  }
  .brand__tagline {
    color: var(--brand-gold);
    font-weight: 500;
    white-space: nowrap;
    letter-spacing: 0.4px;
  }
  .card--front .brand { left: 40px; top: 165px; width: 310px; gap: 8px; }
  .card--front .brand__name { font-size: 22px; letter-spacing: 0.3px; }
  .card--front .brand__dot { width: 16px; height: 16px; }
  .card--front .brand__tagline { font-size: 12px; }

  .card--back .brand { left: 0; top: 160px; width: 690px; gap: 14px; }
  .card--back .brand__name { font-size: 42px; letter-spacing: 1px; gap: 16px; }
  .card--back .brand__dot { width: 28px; height: 28px; }
  .card--back .brand__tagline { font-size: 18px; }

  .divider {
    position: absolute;
    left: 368px; top: 90px;
    width: 2px; height: 214px;
    background: var(--brand-red);
  }
  .contact {
    position: absolute;
    left: 397px; top: 86px;
    color: var(--ink);
  }
  .contact__name {
    color: var(--brand-red);
    font-weight: 700;
    font-size: 27px;
    line-height: 34px;
    letter-spacing: 0.3px;
    white-space: nowrap;
  }
  .contact__role {
    font-size: 17px;
    line-height: 22px;
    margin-top: 2px;
  }
  .contact__address {
    font-size: 17px;
    line-height: 28px;
    margin-top: 17px;
    font-style: normal;
  }
  .contact__list {
    list-style: none;
    margin-top: 11px;
  }
  .contact__item {
    display: flex;
    align-items: center;
    gap: 8px;
    font-size: 17px;
    line-height: 27px;
    white-space: nowrap;
  }
  .contact__icon { width: 15px; height: 15px; flex: none; fill: var(--brand-red); }
</style>
</head>
<body>

<section class="card card--front">
  <div class="brand">
    <div class="brand__name"><span class="brand__dot"></span>Talbrook Roofing</div>
    <p class="brand__tagline">Veteran Owned · Supports Veteran Charities</p>
  </div>
  <div class="divider"></div>
  <div class="contact">
    <h1 class="contact__name">DANIEL HARPER</h1>
    <p class="contact__role">Managing Director</p>
    <address class="contact__address">Your address, City<br>State, Zip 1234</address>
    <ul class="contact__list">
      <li class="contact__item">
        <svg class="contact__icon" viewBox="0 0 16 16" aria-hidden="true"><path d="M1 6c0-2 3-3.5 7-3.5S15 4 15 6v1.5h-3.5V6c-1-.5-6-.5-7 0v1.5H1z"/><path d="M4 8h8l2 6H2z"/></svg>
        123 456 789
      </li>
      <li class="contact__item">
        <svg class="contact__icon" viewBox="0 0 16 16" aria-hidden="true"><path d="M1 3h14v10H1z M2.5 4.2 8 8.6l5.5-4.4z" fill-rule="evenodd"/></svg>
        info@talbrookmail.com
      </li>
      <li class="contact__item">
        <svg class="contact__icon" viewBox="0 0 16 16" aria-hidden="true"><circle cx="8" cy="8" r="7"/><path d="M1 8h14M8 1c-3 3-3 11 0 14M8 1c3 3 3 11 0 14" fill="none" stroke="#fff" stroke-width="1.2"/></svg>
        www.yourwebsite.com
      </li>
    </ul>
  </div>
</section>

<section class="card card--back">
  <div class="brand">
    <div class="brand__name"><span class="brand__dot"></span>Talbrook Roofing</div>
    <p class="brand__tagline">Veteran Owned · Supports Veteran Charities</p>
  </div>
</section>

</body>
</html>
```